Best-selling business author needs Next Craft Line book cover designs

We're launching a series of books and online training videos badged under the "Brightfork Notes - Next Craft Line" brand. The idea is that there are titles for each of the future skills that people will need to survive the robots in the future, eg, Creativity, Critical Thinking Skills, Problem Solving, etc. The exciting job here is to create a series thematic look, and a specific design for the first title, Sharp Prompts.
Hope my brief challenges you, and look forward to your questions and designs.

Target Market(s)

start ups and corporate market (mainly in Asia Pacific) looking to upskill themselves. Probably 18-45 age group, including uni business students, and people working in Meridian 400s.

Industry/Entity Type

Publishing Company

Font styles to use
Serif
Sans Serif
Other font styles liked:
• Felt marker or other 'handcrafted' styles because these will be 'workbook' style publications

Colors
ec1f27
3276b5
00a990
9bcb3c
fbed22
f78f20
6b449b

Requirements
Must have
• Must look professional but not boring or old school.
• Use the "Brightfork Notes Next Craft Line" (logo attached).
• Need category, ie "critical thinking" associated with logo above
• Need title and subtitle of the book, ie "SHARP PROMPTS. How to shape better questions to create explosive breakthroughs."
• All the type you see on sample design, ie reviewers blurb at top, author's name etc.
• Vivid and strong colour schemes to be eye -catching individually but especially strong when lined up on bookshelves together.
• See examples attached for QTV series (competitor) and also a quick design hack by myself to give an idea of what it "might" look like.
• A5 portrait format.
• Spine and Back page will be largely text (with barcode, see example).
• Back page text:
• Heading: Ways to Win the Modern Market with Bold Inquiry Habits.
• - Find out the Sharp Prompts that kick-started empires like NestLoop, Colby Hensel, Beanrowe, Vitalume, Sky Orin, Melodex, Zentrix, Orbely, Tobin Wexley, and even Fundquill.
• - Learn how companies like R&T, Quince, Varlo, AeroMint, Fablon, Lyra, Caravel R3, Movra, and Tulp use Sharp Prompts to develop blockbuster new products, experiences and marketing messages.
• - How to identify and eradicate your cognitive blindspots.
• - How to create a Curiosity Gap (and why that’s so important).
• - Why it’s important to challenge the Status Quo, and how to do it.
• Heading: What if there was a formula for creating Sharp Prompts? There is!
• Get on board this rocket ship with business creativity expert (and best-selling author) Reg Mannix as he guides you through a proven system for creating more insightful, more powerful questions, which point us toward breakthrough solutions, products, and process innovations.
• For the first time, he shares the Sharp Prompts (Discovery Prompt Building Method) here. The same system that he has taught to senior executives from major corporations such as Norvale Bank, Strivon, KessmarFahr, Medwyn, Tolvax, and many other progressive companies.
• Heading: Praise for Sharp Prompts
• “Really enjoyed Sharp Prompts. Like taking a peek into the minds of some of the greatest innovators right as they were asking these SHARP PROMPTS that prompted them to create history!” Rohan Dutt, Head of R&D, Quartel China.
• “Awesome! It’s a great book, I’m a huge fan of the power of questions.” Gavin Hoskins, VP, Norvale Bank.
• "Sharp Prompts is a Sharp Book! This has really helped with both my classroom sessions and consulting projects. Well done!"
• Martin Esterhal, Adj. Professor, The University of Bramcote.
• www.regmannix.example #sharp prompts
• [insert bar code]
Nice to have
• Prefer simple strong bold graphic approach.
• Using photos, or icons to highlight the topic. Please avoid cliches.
Should not have
• Not overly fancy, ornate, or visually complicated.

```html
<!DOCTYPE html>
<html lang="en">
<head>
<meta charset="utf-8">
<title>Brightfork Notes – Next Craft Line covers</title>
<link rel="stylesheet" href="https://fonts.googleapis.com/css2?family=Anton&family=Cinzel:wght@400&family=Open+Sans:ital,wght@0,700;0,800;1,600&display=swap">
<style>
  :root {
    --yellow: #fbe94f;
    --yellow-deep: #f7e23a;
    --teal: #00a990;
    --blue: #3276b5;
    --paper: #ebebeb;
    --ink: #1e1e1e;
    --grey-text: #7a7a7a;
    --credit: #e2622b;
  }
  html, body {
    margin: 0;
    padding: 0;
    width: 1200px;
    height: 644px;
    overflow: hidden;
    background: #ffffff;
  }
  .series {
    display: flex;
    width: 1200px;
    height: 644px;
  }
  .cover {
    position: relative;
    width: 400px;
    height: 644px;
    display: flex;
    flex-direction: column;
    font-family: "Open Sans", Arial, sans-serif;
  }
  .cover--prompts { --accent: var(--yellow); }
  .cover--creativity { --accent: var(--teal); }
  .cover--critical { --accent: var(--blue); }

  .cover__header {
    height: 130px;
    background: var(--accent);
    position: relative;
  }
  .blurb {
    margin: 0;
    padding: 10px 4px 0 26px;
    font-size: 9.8px;
    line-height: 1.5;
    font-style: italic;
    font-weight: 600;
    color: var(--ink);
  }
  .blurb__line {
    display: block;
    white-space: nowrap;
  }
  .blurb__credit {
    font-style: normal;
    font-weight: 700;
    color: var(--credit);
  }
  .imprint {
    position: absolute;
    left: 8px;
    top: 88px;
    display: flex;
    align-items: center;
    gap: 6px;
  }
  .imprint__dot {
    width: 16px;
    height: 16px;
    border-radius: 50%;
    background: var(--ink);
  }
  .imprint__text { line-height: 1; }
  .imprint__name {
    display: block;
    font-size: 19px;
    font-weight: 800;
    color: var(--ink);
    letter-spacing: -0.3px;
  }
  .imprint__line {
    display: block;
    margin-top: 3px;
    font-family: "Cinzel", Georgia, serif;
    font-size: 9px;
    color: var(--ink);
    letter-spacing: 0.4px;
  }

  .cover__body {
    flex: 1;
    background: var(--paper);
    position: relative;
    text-align: center;
  }
  .title {
    margin: 0;
    font-family: "Anton", Impact, sans-serif;
    font-weight: 400;
    color: var(--accent);
    text-shadow: 3px 3px 0 var(--ink);
    line-height: 0.86;
    letter-spacing: 0.5px;
  }
  .cover--prompts .title { padding-top: 10px; font-size: 88px; }
  .cover--creativity .title { padding-top: 30px; font-size: 84px; }
  .cover--critical .title { padding-top: 14px; font-size: 76px; }
  .title__small { font-size: 56px; display: block; margin-top: 6px; }

  .window {
    position: absolute;
    left: 50%;
    top: 168px;
    width: 180px;
    height: 150px;
    transform: translateX(-50%);
  }
  .subtitle {
    position: absolute;
    left: 0;
    right: 0;
    top: 334px;
    margin: 0;
    font-size: 16px;
    font-weight: 800;
    line-height: 1.15;
    color: var(--grey-text);
    letter-spacing: -0.3px;
  }

  .cover__footer {
    height: 126px;
    background: var(--accent);
    text-align: center;
  }
  .author {
    margin: 0;
    padding-top: 54px;
    font-family: "Cinzel", Georgia, serif;
    font-size: 27px;
    line-height: 1;
    color: var(--ink);
    letter-spacing: 0.5px;
  }
  .author-role {
    margin: 8px 0 0;
    font-size: 14px;
    font-weight: 700;
    color: var(--ink);
  }
</style>
</head>
<body>
<main class="series">

  <article class="cover cover--prompts">
    <header class="cover__header">
      <p class="blurb"><span class="blurb__line">“More stimulating than a double shot of cold brew infused coffee.</span><span class="blurb__line">Full of energy, fresh and bright ideas.” - <span class="blurb__credit">DANA FULBRIGHT, FELLOW, CORVEX.</span></span></p>
      <div class="imprint">
        <span class="imprint__dot"></span>
        <span class="imprint__text"><span class="imprint__name">Brightfork Notes</span><span class="imprint__line">NEXT CRAFT LINE &gt;&gt;</span></span>
      </div>
    </header>
    <section class="cover__body">
      <h1 class="title">SHARP<br>PROMPTS</h1>
      <svg class="window" viewBox="0 0 180 150" role="img" aria-label="Torn paper opening showing a question mark with a bomb fuse">
        <polygon points="30,18 72,6 120,14 158,10 170,52 162,92 174,130 120,140 70,146 22,138 8,96 18,60" fill="var(--yellow-deep)"/>
      </svg>
      <p class="subtitle">How to shape better questions<br>to create explosive breakthroughs</p>
    </section>
    <footer class="cover__footer">
      <p class="author">Reg Mannix</p>
      <p class="author-role">Summit x MC/Storyteller/Brightspark</p>
    </footer>
  </article>

  <article class="cover cover--creativity">
    <header class="cover__header">
      <p class="blurb"><span class="blurb__line">“More stimulating than a double shot of cold brew infused coffee.</span><span class="blurb__line">Full of energy, fresh and bright ideas.” - <span class="blurb__credit">DANA FULBRIGHT, FELLOW, CORVEX.</span></span></p>
      <div class="imprint">
        <span class="imprint__dot"></span>
        <span class="imprint__text"><span class="imprint__name">Brightfork Notes</span><span class="imprint__line">NEXT CRAFT LINE &gt;&gt;</span></span>
      </div>
    </header>
    <section class="cover__body">
      <h1 class="title">CREATIVITY</h1>
      <svg class="window" viewBox="0 0 180 150" role="img" aria-label="Torn paper opening showing a crumpled paper light bulb">
        <polygon points="34,14 80,8 126,12 162,20 168,60 160,100 170,136 118,142 66,146 20,136 12,92 22,54" fill="var(--teal)"/>
      </svg>
      <p class="subtitle">How to shape better questions<br>to create explosive breakthroughs</p>
    </section>
    <footer class="cover__footer">
      <p class="author">Reg Mannix</p>
      <p class="author-role">Summit x MC/Storyteller/Brightspark</p>
    </footer>
  </article>

  <article class="cover cover--critical">
    <header class="cover__header">
      <p class="blurb"><span class="blurb__line">“More stimulating than a double shot of cold brew infused coffee.</span><span class="blurb__line">Full of energy, fresh and bright ideas.” - <span class="blurb__credit">DANA FULBRIGHT, FELLOW, CORVEX.</span></span></p>
      <div class="imprint">
        <span class="imprint__dot"></span>
        <span class="imprint__text"><span class="imprint__name">Brightfork Notes</span><span class="imprint__line">NEXT CRAFT LINE &gt;&gt;</span></span>
      </div>
    </header>
    <section class="cover__body">
      <h1 class="title">CRITICAL<span class="title__small">THINKING SKILLS</span></h1>
      <svg class="window" viewBox="0 0 180 150" role="img" aria-label="Torn paper opening showing a glowing network brain">
        <polygon points="28,16 76,8 124,12 164,18 168,62 158,104 168,136 114,144 62,144 18,134 10,90 20,50" fill="var(--blue)"/>
      </svg>
      <p class="subtitle">How to shape better questions<br>to create explosive breakthroughs</p>
    </section>
    <footer class="cover__footer">
      <p class="author">Reg Mannix</p>
      <p class="author-role">Summit x MC/Storyteller/Brightspark</p>
    </footer>
  </article>

</main>
</body>
</html>
```